IRON SASH VIGOUR CERTIFICATE

Carrowby Hapkido Inc is wanting to introduce a fitness system based upon certificates reflecting rank; White - Yellow - Blue - Red - Black.

The Certificate "MUST" have on it "IRON SASH VIGOUR"

The Certificate "MUST" have a martial arts theme!

The Certificate "MUST" reflect the fitness requirements for each rank.

The colour scheme for each Certificate "MUST" reflect the belt rank

The Certificate must include at least one martial arts graphic / motif

The certificate must have the Carrowby HKD LOGO

We will need a certificate template that can be for all levels but reflect the rank and fitness level. The certificate can be either traditional or modern style but must reflect a martial art themes. The certificate must have the Carrowby Hapkido logo incorporated into the certificate with signature space for senior instructors Dan Pellow & Sorna Vick-Pellow. The certificates should be eye catching and exciting to look at. It should bold and incorporate martial art motifs etc The fitness requirements are not onerous and the certificate system is created to incentivise physical activity and correct technique rather than creating an impossible standards only Olympians can achieve. The majority of our students are upper primary and lower secondary from 11yr-15yrs. Certificate should be youthful but not silly. The certificate template will be reproduced for each colour belt.White = 10 push ups 10 Sit ups 10 squats 10 Jumping Jacks 20 sec plank 400m continuous run Demonstrate beginner stretching techniqueYellow = 20 push ups 20 sit ups 20 squats 20 Jumping Jacks 40 Sec plank 800m continuous run Demonstrate intermediate stretching techniqueBlue = 30 push ups 30 sit ups 30 squats 30 Jumping Jacks 60 Sec plank 1200m continuous run Demonstrate intermediate stretching techniqueRed = 40 push ups 40 sit ups 40 squats 40 Jumping Jacks 75sec plank 1600m run Demonstrate advanced stretching techniqueBlack = 50 push ups 50 sit ups 50 squats 50 Jumping jacks 90 sec planks 2000m continuous run Demonstrate advanced stretching technique
Updates

HI Designers, Please go for modern and professionals. Several designs have used traditional motifs of water dragons or lattice bordering. This looks old school. Please do not use martial art silhouettes as it looks amateur. Definately looking for upmarket high quality presentations.

Logo Text

IRON SASH VIGOUR

Font styles to use
Decorative

Colors

Designer to choose colors to be used in the design.

Requirements
Must have
• This will be a template foe all coloured ranks of fitness, Be bold, memorable, should be themed to martial arts etc

```html
<!DOCTYPE html>
<html lang="en">
<head>
<meta charset="utf-8">
<title>Carrowby Hapkido – Iron Sash Vigour Certificate</title>
<link rel="stylesheet" href="https://fonts.googleapis.com/css2?family=Libre+Baskerville:wght@400;700&family=Great+Vibes&family=Open+Sans:wght@400&display=swap">
<style>
  :root {
    --backdrop: #3a3b3d;
    --paper: #ffffff;
    --navy: #252a3a;
    --red: #e8202a;
    --blush: #f8d6d8;
    --border-tone: #c4c8d2;
    --rule: #6b5a55;
  }
  * { margin: 0; padding: 0; box-sizing: border-box; }
  html, body {
    width: 1200px;
    height: 925px;
    overflow: hidden;
    background: var(--backdrop);
  }
  .canvas {
    position: relative;
    width: 1200px;
    height: 925px;
  }
  .frame-art {
    position: absolute;
    left: 0; top: 0;
  }
  .programme-name {
    position: absolute;
    left: 0; width: 1200px; top: 150px;
    text-align: center;
    font-family: "Libre Baskerville", serif;
    font-weight: 700;
    font-size: 14px;
    letter-spacing: 5px;
    color: var(--navy);
  }
  .rank-label {
    position: absolute;
    left: 190px; top: 366px;
    width: 72px;
    text-align: center;
    font-family: "Libre Baskerville", serif;
    font-size: 13px;
    letter-spacing: 0.5px;
    color: var(--paper);
  }
  .club-name {
    position: absolute;
    left: 900px; top: 264px;
    width: 148px;
    text-align: center;
    font-family: "Libre Baskerville", serif;
    font-weight: 700;
    font-size: 17px;
    line-height: 1.35;
    color: var(--paper);
  }
  .subtitle {
    position: absolute;
    left: 0; width: 1200px; top: 346px;
    text-align: center;
    font-family: "Libre Baskerville", serif;
    font-weight: 700;
    font-size: 22px;
    letter-spacing: 1.5px;
    color: var(--navy);
  }
  .presented {
    position: absolute;
    left: 0; width: 1200px; top: 412px;
    text-align: center;
    font-family: "Libre Baskerville", serif;
    font-size: 21px;
    letter-spacing: 0.4px;
    color: var(--red);
  }
  .recipient {
    position: absolute;
    left: 0; width: 1200px; top: 480px;
    text-align: center;
    font-family: "Great Vibes", cursive;
    font-size: 64px;
    color: var(--red);
  }
  .rank-title {
    position: absolute;
    left: 0; width: 1200px; top: 582px;
    text-align: center;
    font-family: "Libre Baskerville", serif;
    font-size: 16px;
    letter-spacing: 0.5px;
    color: var(--navy);
  }
  .requirements {
    position: absolute;
    left: 340px; width: 520px; top: 607px;
    text-align: center;
    font-family: "Open Sans", sans-serif;
    font-size: 14px;
    line-height: 18px;
    color: var(--navy);
  }
  .sign-label {
    position: absolute;
    top: 732px;
    width: 210px;
    text-align: center;
    font-family: "Open Sans", sans-serif;
    font-size: 16px;
    color: var(--navy);
  }
  .sign-label.date { left: 236px; }
  .sign-label.signature { left: 754px; }
</style>
</head>
<body>
<main class="canvas">
  <svg class="frame-art" width="1200" height="925" viewBox="0 0 1200 925">
    <defs>
      <linearGradient id="beltTone" x1="0" y1="0" x2="0" y2="1">
        <stop offset="0" stop-color="#3a4052"/>
        <stop offset="1" stop-color="#252a3a"/>
      </linearGradient>
    </defs>

    <rect class="paper" x="56" y="58" width="1086" height="808" fill="var(--paper)"/>
    <rect class="outer-rule" x="70" y="71" width="1060" height="783" fill="none" stroke="var(--navy)" stroke-width="2"/>
    <path class="border-band" role="img" aria-label="Ornamental scrollwork border"
          fill="var(--border-tone)" fill-rule="evenodd"
          d="M78 79 H1122 V846 H78 Z M114 114 H1086 V810 H114 Z"/>
    <rect class="inner-rule" x="120" y="123" width="960" height="679" fill="none" stroke="var(--navy)" stroke-width="2"/>
    <rect class="inner-rule-fine" x="128" y="130" width="944" height="664" fill="none" stroke="var(--navy)" stroke-width="1"/>

    <polygon class="ribbon-left" points="190,130 262,130 262,422 226,410 190,422" fill="var(--red)"/>
    <polygon class="ribbon-right" points="938,130 1010,130 1010,422 974,410 938,422" fill="var(--red)"/>

    <rect class="belt-art" role="img" aria-label="Tied martial arts belt illustration"
          x="146" y="228" width="162" height="124" rx="40" fill="url(#beltTone)"/>

    <circle class="club-badge" cx="974" cy="292" r="86" fill="var(--navy)" stroke="var(--paper)" stroke-width="4"/>

    <ellipse class="title-flourish" role="img" aria-label="Red calligraphic flourish"
             cx="600" cy="216" rx="110" ry="26" fill="var(--blush)"/>

    <text class="title" x="600" y="331" text-anchor="middle" textLength="500" lengthAdjust="spacingAndGlyphs"
          font-family="'Libre Baskerville', serif" font-weight="700" font-size="72" fill="var(--navy)">CERTIFICATE</text>

    <path class="swash-left" d="M342 368 C 390 362, 420 352, 468 360" fill="none" stroke="var(--red)" stroke-width="1.6"/>
    <path class="swash-left" d="M362 366 C 400 357, 436 354, 468 361" fill="none" stroke="var(--red)" stroke-width="0.8"/>
    <path class="swash-right" d="M858 368 C 810 362, 780 352, 732 360" fill="none" stroke="var(--red)" stroke-width="1.6"/>
    <path class="swash-right" d="M838 366 C 800 357, 764 354, 732 361" fill="none" stroke="var(--red)" stroke-width="0.8"/>

    <line class="name-rule" x1="430" y1="566" x2="770" y2="566" stroke="var(--navy)" stroke-width="2"/>
    <line class="date-rule" x1="236" y1="721" x2="446" y2="721" stroke="var(--rule)" stroke-width="1"/>
    <line class="signature-rule" x1="754" y1="721" x2="964" y2="721" stroke="var(--rule)" stroke-width="1"/>
  </svg>

  <div class="programme-name">IRON SASH VIGOUR</div>
  <div class="rank-label">YELLOW</div>
  <div class="club-name">Carrowby<br>Hapkido</div>

  <div class="subtitle">OF COMPLETION</div>
  <div class="presented">THIS CERTIFICATE IS PROUDLY PRESENTED TO</div>
  <div class="recipient">Name Here</div>
  <div class="rank-title">WHITE BELT</div>
  <p class="requirements">10 push ups 10 Sit ups 10 squats 10 Jumping Jacks 20 sec plank 400m continuous run Demonstrate beginner stretching technique</p>

  <div class="sign-label date">DATE</div>
  <div class="sign-label signature">SIGNATURE</div>
</main>
</body>
</html>
```